Web Design Project

We have a website in beta that needs updating and are looking for a freash new look for the Home page including Logo.
Our company is called " Ka Ze Lo " we specialize in classified advertising using video. Our consumers will be businesses selling a product or service. Please visit www.kazelo.com
Our aim past this point is to engage a developer to write the code based on the best design. Our target market is the U.S and I have included some of the landing pages to give you a better idea of what we are trying to acheive

http://www.kazelo.com/
http://www.kazelo.com/cars_home.php
http://www.kazelo.com/boats.php
http://www.kazelo.com/electronic.php
http://www.kazelo.com/realestate.php
http://www.kazelo.com/roommates.php

Target Market(s)

20-35 yr old people who are connected to the internet via mobile phone and use social media on a daily/weekly basis

Industry/Entity Type

Advertising

Requirements
Must have
• We would like to use lots of images to convey it is a video driven website business
Nice to have
• Logo to incorporate same theme of website ( ie ) you are here to watch videos of thinhs to buy & sell
Should not have
• This is to be a freash new site with large type and bold fonts

```html
<!DOCTYPE html>
<html lang="en">
<head>
<meta charset="utf-8">
<title>Ka Ze Lo – Video Classifieds</title>
<link rel="stylesheet" href="https://fonts.googleapis.com/css2?family=Raleway:wght@400;500;600;700;800&display=swap">
<style>
:root{
  --navy-deep:#0b1a3c;
  --navy:#12275a;
  --navy-mid:#1b3470;
  --footer:#0f1f4a;
  --sky:#1fa6ee;
  --sky-light:#35c0fb;
  --sky-dark:#1289d6;
  --orange:#f7861d;
  --orange-light:#ffa236;
  --orange-dark:#e86a0a;
  --white:#ffffff;
  --link:#6f9ad8;
  --tab:#1e3a78;
  --tab-text:#9db8e6;
  --grey-line:#cfd3da;
}
*{box-sizing:border-box;margin:0;padding:0}
html,body{width:1140px;height:1200px;overflow:hidden;background:var(--navy-deep)}
body{font-family:"Raleway",Arial,sans-serif;color:var(--white)}
.page{position:relative;width:1140px;height:1200px;overflow:hidden}

/* Header / featured band */
.top{position:absolute;left:0;top:0;width:1140px;height:625px;
  background:radial-gradient(ellipse at 50% 30%,#1b3470 0%,#102456 45%,#0a1838 100%)}
.brand{position:absolute;left:125px;top:22px}
.brand-name{font-size:32px;font-weight:700;line-height:36px;color:var(--white)}
.brand-tag{font-size:11px;font-weight:600;line-height:13px;margin-top:4px}
.brand-tag strong{display:block;font-size:17px;font-weight:700;line-height:20px}
.langs{position:absolute;right:124px;top:14px;font-size:11px;color:var(--tab-text)}
.langs b{color:var(--white);font-weight:700}
.actions{position:absolute;left:503px;top:46px;display:flex;gap:9px}
.btn{height:35px;border-radius:3px;font-size:13px;font-weight:700;display:flex;align-items:center;gap:8px;padding:0 14px}
.btn-create{width:149px;background:linear-gradient(var(--orange-light),var(--orange-dark));color:var(--white)}
.btn-sign{width:97px;background:linear-gradient(#fff,#dfe2e7);color:#222}
.search{width:248px;height:35px;border-radius:3px;background:var(--white);border:3px solid #d8dde5;display:flex;align-items:center;gap:8px;padding:0 10px;font-size:12px;color:#777}
.nav{position:absolute;left:125px;top:113px;width:891px;height:40px;display:flex;border-radius:3px;overflow:hidden;
  background:linear-gradient(var(--sky-light),var(--sky-dark))}
.nav a{display:flex;align-items:center;justify-content:center;gap:4px;font-size:13px;font-weight:600;color:var(--white);text-decoration:none;border-right:1px solid rgba(255,255,255,.25)}
.nav a:last-child{border-right:none}
.featured-title{position:absolute;left:125px;top:180px;display:flex;align-items:center;gap:12px;font-size:22px;font-weight:600}
.tabs{position:absolute;right:124px;top:182px;display:flex;gap:8px}
.tab{height:28px;padding:0 14px;border-radius:2px;font-size:12px;display:flex;align-items:center;background:var(--tab);color:var(--tab-text)}
.tab.active{background:var(--sky);color:var(--white)}
.grid{position:absolute;left:125px;top:242px;width:891px;display:grid;grid-template-columns:repeat(4,210px);column-gap:17px;row-gap:18px}
.thumb{position:relative;height:168px;background:var(--white);border-radius:4px;padding:6px}
.thumb-media{width:100%;height:100%}
.play{position:absolute;left:50%;top:50%;width:26px;height:26px;margin:-13px 0 0 -13px}
.m-boat{background:linear-gradient(#7fb4e4 0%,#cfe3f2 45%,#3aa3b8 70%,#11808f 100%)}
.m-house{background:linear-gradient(#4e8fdc 0%,#aecbea 40%,#c8c3b4 60%,#4f8c36 100%)}
.m-suv{background:linear-gradient(#c9ccd2,#8c9098 60%,#1a1c20 100%)}
.m-tech{background:linear-gradient(#1a1a1a,#4b4b4b 60%,#0e0e0e)}
.m-plane{background:linear-gradient(#6a7ea8 0%,#b8a3b5 50%,#d9876d 100%)}
.m-concept{background:linear-gradient(#aebfd0,#5e6c7c 60%,#2b3138)}
.m-room{background:linear-gradient(#c7b89a,#7d8f4a 60%,#5b6f2e)}
.m-move{background:linear-gradient(#e4d7c1,#c5a987 60%,#e9e4da)}

/* How it works */
.how{position:absolute;left:0;top:625px;width:1140px;height:387px;background:linear-gradient(#ffffff,#e7e9ec)}
.how-rule{position:absolute;left:125px;top:42px;width:891px;height:2px;background:var(--grey-line)}
.ribbon{position:absolute;left:470px;top:20px;width:208px;height:46px}
.ribbon span{position:absolute;inset:0;display:flex;align-items:center;justify-content:center;font-size:21px;font-weight:600;color:var(--white)}
.step{position:absolute;top:82px;width:266px}
.step-photo{margin:0 auto;height:212px;background:linear-gradient(#f4f4f4,#2a2e38 55%,#16181e)}
.step-btn{position:relative;margin-top:-6px;width:266px;height:70px}
.step-btn span{position:absolute;left:0;top:10px;width:232px;height:50px;display:flex;align-items:center;justify-content:center;font-size:22px;font-weight:600;color:var(--white)}
.s1{left:125px}.s1 .step-photo{width:150px}
.s2{left:437px}.s2 .step-photo{width:248px;background:linear-gradient(#f5f5f5,#b8c3d4 45%,#2a2b30)}
.s3{left:749px}.s3 .step-photo{width:232px}

/* Footer */
.foot{position:absolute;left:0;top:1012px;width:1140px;height:188px;background:var(--footer);border-top:3px solid var(--orange)}
.col{position:absolute;top:30px}
.col h4{font-size:15px;font-weight:600;margin-bottom:12px;color:var(--white)}
.col a{display:block;font-size:12px;line-height:21.6px;color:var(--link);text-decoration:none}
.social{display:flex;gap:5px;margin-top:10px}
.social i{width:29px;height:29px;border-radius:50%;background:#7f9fd6}
.copy{font-size:12px;line-height:17px;color:var(--link);margin-top:14px}
</style>
</head>
<body>
<div class="page">
  <header class="top">
    <div class="brand">
      <div class="brand-name">Ka Ze Lo</div>
      <div class="brand-tag">Buy and sell through the<strong>#1 Video Classifieds</strong></div>
    </div>
    <div class="langs"><b>EN</b> | GE | FR | SP | IT | SW</div>
    <div class="actions">
      <div class="btn btn-create">
        <svg width="14" height="14" viewBox="0 0 14 14"><path d="M2 12l1-4 7-7 3 3-7 7z" fill="#fff"/></svg>CREATE AN AD</div>
      <div class="btn btn-sign">
        <svg width="13" height="14" viewBox="0 0 13 14"><circle cx="6.5" cy="4" r="3.2" fill="#222"/><path d="M0 14c0-4 3-6 6.5-6S13 10 13 14z" fill="#222"/></svg>SIGN IN</div>
      <div class="search">
        <svg width="14" height="14" viewBox="0 0 14 14"><circle cx="6" cy="6" r="4.5" stroke="#666" stroke-width="1.8" fill="none"/><path d="M9.5 9.5L13 13" stroke="#666" stroke-width="1.8"/></svg>Search...</div>
    </div>
    <nav class="nav">
      <a href="#" style="width:99px">CAR</a>
      <a href="#" style="width:114px">BOATS</a>
      <a href="#" style="width:162px">ELECTRONICS</a>
      <a href="#" style="width:156px">REAL ESTATE</a>
      <a href="#" style="width:157px">ROOMMATES</a>
      <a href="#" style="width:203px">OTHER CATEGORIES
        <svg width="7" height="10" viewBox="0 0 7 10"><path d="M0 0l7 5-7 5z" fill="#fff"/></svg></a>
    </nav>
    <h2 class="featured-title">
      <svg width="30" height="30" viewBox="0 0 30 30"><circle cx="12" cy="12" r="9.5" stroke="#fff" stroke-width="3.5" fill="none"/><path d="M19 19l8 8" stroke="#fff" stroke-width="4" stroke-linecap="round"/></svg>
      Browse Featured on Ka Ze Lo</h2>
    <div class="tabs">
      <div class="tab active">Most Viewed</div>
      <div class="tab">Most Recent</div>
      <div class="tab">Most Interesting</div>
    </div>
    <div class="grid">
      <div class="thumb"><div class="thumb-media m-boat" role="img" aria-label="Motor yacht cruising on turquoise water"></div><svg class="play" viewBox="0 0 26 26"><circle cx="13" cy="13" r="13" fill="#fff"/><path d="M11 8l5 5-5 5" stroke="#333" stroke-width="2" fill="none"/></svg></div>
      <div class="thumb"><div class="thumb-media m-house" role="img" aria-label="Two-storey suburban house with lawn"></div><svg class="play" viewBox="0 0 26 26"><circle cx="13" cy="13" r="13" fill="#fff"/><path d="M11 8l5 5-5 5" stroke="#333" stroke-width="2" fill="none"/></svg></div>
      <div class="thumb"><div class="thumb-media m-suv" role="img" aria-label="Black luxury SUV"></div><svg class="play" viewBox="0 0 26 26"><circle cx="13" cy="13" r="13" fill="#fff"/><path d="M11 8l5 5-5 5" stroke="#333" stroke-width="2" fill="none"/></svg></div>
      <div class="thumb"><div class="thumb-media m-tech" role="img" aria-label="Home electronics: screens, laptop and speakers"></div><svg class="play" viewBox="0 0 26 26"><circle cx="13" cy="13" r="13" fill="#fff"/><path d="M11 8l5 5-5 5" stroke="#333" stroke-width="2" fill="none"/></svg></div>
      <div class="thumb"><div class="thumb-media m-plane" role="img" aria-label="Passenger jet flying at sunset"></div><svg class="play" viewBox="0 0 26 26"><circle cx="13" cy="13" r="13" fill="#fff"/><path d="M11 8l5 5-5 5" stroke="#333" stroke-width="2" fill="none"/></svg></div>
      <div class="thumb"><div class="thumb-media m-concept" role="img" aria-label="Silver concept sports car in a glass hall"></div><svg class="play" viewBox="0 0 26 26"><circle cx="13" cy="13" r="13" fill="#fff"/><path d="M11 8l5 5-5 5" stroke="#333" stroke-width="2" fill="none"/></svg></div>
      <div class="thumb"><div class="thumb-media m-room" role="img" aria-label="Young woman seated on a green sofa in a shared room"></div><svg class="play" viewBox="0 0 26 26"><circle cx="13" cy="13" r="13" fill="#fff"/><path d="M11 8l5 5-5 5" stroke="#333" stroke-width="2" fill="none"/></svg></div>
      <div class="thumb"><div class="thumb-media m-move" role="img" aria-label="Two roommates sitting among moving boxes"></div><svg class="play" viewBox="0 0 26 26"><circle cx="13" cy="13" r="13" fill="#fff"/><path d="M11 8l5 5-5 5" stroke="#333" stroke-width="2" fill="none"/></svg></div>
    </div>
  </header>

  <section class="how">
    <div class="how-rule"></div>
    <div class="ribbon">
      <svg width="208" height="46" viewBox="0 0 208 46"><path d="M0 0h208l-12 23 12 23H0l12-23z" fill="#162c63"/></svg>
      <span>How It Works</span>
    </div>
    <div class="step s1">
      <div class="step-photo" role="img" aria-label="Person filming with a video camera"></div>
      <div class="step-btn"><svg width="266" height="70" viewBox="0 0 266 70"><defs><linearGradient id="og" x1="0" y1="0" x2="0" y2="1"><stop offset="0" stop-color="#ffa236"/><stop offset="1" stop-color="#e86a0a"/></linearGradient></defs><path d="M0 10h212V0l54 35-54 35V60H0z" fill="url(#og)"/></svg><span>CREATE IT</span></div>
    </div>
    <div class="step s2">
      <div class="step-photo" role="img" aria-label="Person at a laptop uploading a video"></div>
      <div class="step-btn"><svg width="266" height="70" viewBox="0 0 266 70"><path d="M0 10h212V0l54 35-54 35V60H0z" fill="url(#og)"/></svg><span>UPLOAD IT</span></div>
    </div>
    <div class="step s3">
      <div class="step-photo" role="img" aria-label="Two business people shaking hands on a sale"></div>
      <div class="step-btn"><svg width="266" height="70" viewBox="0 0 266 70"><path d="M0 10h212V0l54 35-54 35V60H0z" fill="url(#og)"/></svg><span>SELL IT</span></div>
    </div>
  </section>

  <footer class="foot">
    <div class="col" style="left:125px"><h4>Buy / Browse</h4><a href="#">Car</a><a href="#">Boats</a><a href="#">Electronics</a><a href="#">Roommates</a><a href="#">Othres</a></div>
    <div class="col" style="left:310px"><h4>Sell</h4><a href="#">Starting Selling</a><a href="#">Login</a><a href="#">Shooting Video</a><a href="#">Uploading Video</a><a href="#">Buying</a></div>
    <div class="col" style="left:505px"><h4>Info</h4><a href="#">VBlog</a><a href="#">FAQs</a><a href="#">Terms Of Use</a><a href="#">Privancy Policy</a><a href="#">Buyer/Seller Safety</a></div>
    <div class="col" style="left:706px"><h4>Contact</h4><a href="#">Feedback Form</a><a href="#">Referral Pogram</a><a href="#">Business Register</a><a href="#">Subscription</a><a href="#">Contact Us</a></div>
    <div class="col" style="left:873px"><h4>Stay Connect</h4>
      <div class="social"><i></i><i></i><i></i></div>
      <p class="copy">Copyright © 2013 Video Classifieds.<br>All Rights Reserved.</p>
    </div>
  </footer>
</div>
</body>
</html>
```